VORANTO POWER Solar Website Design

I need a website designed for my solar company VORANTO Power. Something that looks very professional and keeps the customer engaged. I am including my company flyer to give you all the information you need to design the page. Please use exact wording as it is written on the flyer and pictures somewhat similar to what’s on the flyer as well.

I have also included my company logos in various color styles. So please include the logo.

The website domain is www.vorantopower.org

And I need to make sure the website is formatted for phone, tablet and computer.

Target Market(s)

Residential Home Owners

Industry/Entity Type

Solar

Coding

Coded - Design and coding required

Number of Pages Required

4 page

Requirements
Nice to have
• I would like web page to have inter active tabs. So when they click on a picture like I have on the flyer a drop down tab shows the explanation (text). This website from another company is a good example of what I mean. https://www.brelvatek.com. Please click to see.

```html
<!DOCTYPE html>
<html lang="en">
<head>
<meta charset="utf-8">
<title>Voranto Power</title>
<link href="https://fonts.googleapis.com/css2?family=Roboto:wght@300;400;500;700;900&display=swap" rel="stylesheet">
<style>
:root{
  --orange:#f7a21b;
  --navy:#0d2466;
  --band:#132c63;
  --band-dark:#0b1c45;
  --ink:#1d1d1d;
  --muted:#555;
  --white:#fff;
}
*{box-sizing:border-box;margin:0;padding:0}
html,body{width:1200px;height:4298px;overflow:hidden}
body{position:relative;font-family:'Roboto',sans-serif;color:var(--ink);background:#fff}
.abs{position:absolute}
.btn{position:absolute;display:flex;align-items:center;justify-content:center;gap:8px;font-size:15px;font-weight:700;color:#fff;text-transform:uppercase;letter-spacing:.2px}
.btn::after{content:"";border-left:7px solid currentColor;border-top:6px solid transparent;border-bottom:6px solid transparent}
.btn-orange{background:var(--orange)}
.btn-navy{background:var(--navy)}

/* header */
.topbar{position:absolute;left:420px;top:0;width:780px;height:45px;background:var(--orange);clip-path:polygon(0 0,100% 0,100% 100%,26px 100%);display:flex;align-items:center;gap:40px;padding-left:105px;color:#fff;font-size:15px;font-weight:500}
.topbar span{display:flex;align-items:center;gap:10px}
.brand{position:absolute;left:108px;top:36px;font-size:30px;font-weight:500;letter-spacing:2px;color:#222;line-height:1}
.brand small{display:block;font-size:10px;letter-spacing:7px;text-align:center;margin-top:4px}
.nav{position:absolute;left:485px;top:66px;display:flex;gap:39px;font-size:15.5px;font-weight:500;color:#222}
.nav .active{color:var(--orange)}

/* hero */
.hero-title{position:absolute;left:110px;top:188px;color:#fff;font-size:44px;line-height:52px;font-weight:700}
.hero-title .light{font-weight:300}
.hero-sub{position:absolute;left:110px;top:353px;width:440px;color:#fff;font-size:15px;line-height:26px}

/* sections */
.h2{position:absolute;left:0;width:1200px;text-align:center;font-size:33px;font-weight:400;text-transform:uppercase}
.h2 b{font-weight:700}
.h2.under::after{content:"";display:block;width:62px;height:3px;background:var(--orange);margin:12px auto 0}
.about-title{position:absolute;left:629px;top:796px;font-size:33px;text-transform:uppercase}
.about-title b{font-weight:700}
.about-text{position:absolute;left:629px;top:862px;width:466px;font-size:13.6px;line-height:25.8px;color:#333}
.about-text b{font-weight:500;color:#111}

.band{position:absolute;left:0;width:1200px}
.why-box{position:absolute;width:309px;height:160px;border:1.5px solid rgba(255,255,255,.75);text-align:center;color:#fff}
.why-box.on{border:3px solid var(--orange)}
.why-box.on .why-name{color:var(--orange)}
.why-icon{position:absolute;left:50%;top:-40px;width:80px;height:80px;margin-left:-40px;border-radius:50%;background:var(--orange);display:flex;align-items:center;justify-content:center}
.why-box.on .why-icon{background:var(--navy);border:3px solid #fff}
.why-name{position:absolute;left:0;right:0;top:72px;font-size:19px;font-weight:500}
.why-more{position:absolute;left:0;right:0;top:110px;font-size:16px;font-weight:500;color:var(--orange);display:flex;justify-content:center;align-items:center;gap:8px}
.why-more::after{content:"";border-left:7px solid var(--orange);border-top:6px solid transparent;border-bottom:6px solid transparent}

.svc-card{position:absolute;top:2211px;width:309px;height:439px;background:#fff;border-radius:8px;box-shadow:0 2px 14px rgba(0,0,0,.14);text-align:center}
.svc-img{position:absolute;left:12px;top:12px;width:285px;height:182px;border-radius:8px}
.svc-icon{position:absolute;left:122px;top:158px;width:64px;height:64px;border-radius:50%;background:var(--orange);border:3px solid #fff;display:flex;align-items:center;justify-content:center}
.svc-icon.dark{background:var(--navy)}
.svc-name{position:absolute;left:14px;right:14px;top:243px;font-size:16.5px;font-weight:700;line-height:25px;text-transform:uppercase}
.svc-text{position:absolute;left:14px;right:14px;font-size:13.6px;line-height:25px;color:#444}
.arrow-c{position:absolute;top:2412px;width:26px;height:26px;border:1.5px solid #333;border-radius:50%;display:flex;align-items:center;justify-content:center}

.step{position:absolute;top:2979px;width:92px;height:92px;border:3px solid var(--orange);border-radius:50%;display:flex;align-items:center;justify-content:center}
.step-label{position:absolute;top:3094px;width:260px;text-align:center;color:#fff;font-size:20.5px;line-height:34px}

.ci{position:absolute;left:138px;width:80px;height:80px;border-radius:50%;background:var(--orange);display:flex;align-items:center;justify-content:center}
.ci-label{position:absolute;left:245px;font-size:14.5px;font-weight:700}
.ci-text{position:absolute;left:245px;font-size:14.5px;line-height:26px;color:#222}
.field{position:absolute;background:#fff;box-shadow:0 1px 8px rgba(0,0,0,.16);font-size:14px;color:#666;padding:15px 16px}

.footer{position:absolute;left:0;top:3872px;width:1200px;height:426px;background:var(--band-dark);color:#fff}
.f-h{position:absolute;top:64px;font-size:22px;font-weight:500}
.f-links{position:absolute;left:491px;top:95px;list-style:none;font-size:15px;line-height:32.5px}
.f-links li{display:flex;align-items:center;gap:12px}
.f-links li::before{content:"➜";font-size:13px}
.f-links li:first-child{font-weight:700}
.f-dot{position:absolute;left:733px;width:38px;height:38px;border-radius:50%;background:var(--orange);display:flex;align-items:center;justify-content:center}
.f-text{position:absolute;left:790px;font-size:15px;line-height:31px}
.social{position:absolute;top:4132px;width:30px;height:30px;border-radius:50%;border:1.5px solid #fff}
</style>
</head>
<body>

<!-- header -->
<div class="brand">VORANTO<small>POWER</small></div>
<div class="topbar">
  <span><svg width="20" height="20" viewBox="0 0 24 24" fill="#fff"><path d="M6.6 10.8a15 15 0 006.6 6.6l2.2-2.2a1 1 0 011-.25 11 11 0 003.5.56 1 1 0 011 1V20a1 1 0 01-1 1A17 17 0 013 4a1 1 0 011-1h3.5a1 1 0 011 1 11 11 0 00.56 3.5 1 1 0 01-.25 1z"/></svg>PHONE: +1 555 0100 2020</span>
  <span><svg width="22" height="16" viewBox="0 0 22 16" fill="#fff"><path d="M0 0h22v16H0z" opacity=".9"/><path d="M0 0l11 9 11-9" stroke="#f7a21b" stroke-width="2" fill="none"/></svg>EMAIL: info@vorantopower.org</span>
</div>
<nav class="nav"><span class="active">HOME</span><span>ABOUT US</span><span>SERVICES</span><span>WHY CHOOSE US</span><span>CONTACT US</span></nav>

<!-- hero -->
<svg class="abs" style="left:0;top:103px" width="1200" height="592" viewBox="0 0 1200 592">
  <defs>
    <linearGradient id="heroSky" x1="0" y1="0" x2="1" y2="1">
      <stop offset="0" stop-color="#2c2a26"/><stop offset=".5" stop-color="#5c5448"/><stop offset="1" stop-color="#3a3833"/>
    </linearGradient>
  </defs>
  <polygon points="0,0 1200,0 1200,427 600,556 0,427" fill="url(#heroSky)" role="img" aria-label="Modern house with solar panels on the roof and an electric car in the driveway at dusk"/>
  <polygon points="190,475 600,560 1010,475 1010,478 600,590 190,478" fill="#f7a21b"/>
  <rect x="591" y="496" width="18" height="26" rx="9" fill="none" stroke="#fff" stroke-width="1.5"/>
  <line x1="600" y1="502" x2="600" y2="508" stroke="#fff" stroke-width="1.5"/>
</svg>
<h1 class="hero-title"><span class="light">WE MAKE SWITCHING</span><br>TO SOLAR SO SIMPLE<br>IT'S SMART!</h1>
<p class="hero-sub">By Swithching to Solar Not Only Are You Saving Money but You Are Also Saving the Planet</p>
<div class="btn btn-orange" style="left:112px;top:418px;width:145px;height:49px">Get Started</div>

<!-- about -->
<svg class="abs" style="left:150px;top:804px" width="374" height="374" role="img" aria-label="Solar installer in a hard hat working on a rooftop solar panel">
  <defs><linearGradient id="aboutImg" x1="0" y1="0" x2="0" y2="1"><stop offset="0" stop-color="#3f7fc9"/><stop offset=".55" stop-color="#1d3f7a"/><stop offset="1" stop-color="#263450"/></linearGradient></defs>
  <circle cx="187" cy="187" r="187" fill="url(#aboutImg)"/>
</svg>
<h2 class="about-title"><b>About</b> Us</h2>
<p class="about-text"><b>Voranto Power</b> powered by <b>Brightfield Smart Energy is America's</b> leading solar company. Listed by Apex 5000 as the 14th Fastest growing company Nation wide in 2024 and the top solar company to work with. We have helped thousands of home owners Nation wide save thousands with our solar solutions. Our premium, high-output solar panels are designed for maximum energy efficiency, so you can stop over paying on your electric bills each month. We provide a white glove service for all of our customers ensuring the entire project is handled from A-Z by our expert professional installers, designers and electricians giving you the best solar installation experience possible.</p>
<div class="btn btn-navy" style="left:629px;top:1138px;width:145px;height:49px">Learn More</div>

<!-- why choose us -->
<div class="band" style="top:1318px;height:718px;background:linear-gradient(180deg,#142d66,#1a3470 50%,#10265a)" role="img" aria-label="Dark blue tinted background of a house at night"></div>
<h2 class="h2 under" style="top:1400px;color:#fff"><b>Why Choose</b> Us?</h2>

<div class="why-box" style="left:110px;top:1536px"><div class="why-icon"><svg width="40" height="40" viewBox="0 0 40 40" fill="none" stroke="#fff" stroke-width="2"><circle cx="20" cy="20" r="7"/><circle cx="20" cy="20" r="13" stroke-dasharray="4 3"/></svg></div><div class="why-name">Quality Workmanship</div><div class="why-more">Learn More</div></div>
<div class="why-box on" style="left:445px;top:1536px"><div class="why-icon"><svg width="40" height="40" viewBox="0 0 40 40" fill="none" stroke="#fff" stroke-width="2"><circle cx="17" cy="18" r="9"/><path d="M24 25l8 8"/></svg></div><div class="why-name">Expertise</div><div class="why-more">Learn More</div></div>
<div class="why-box" style="left:780px;top:1536px"><div class="why-icon"><svg width="40" height="40" viewBox="0 0 40 40" fill="none" stroke="#fff" stroke-width="2"><circle cx="22" cy="15" r="9"/><path d="M5 30h10l8 4 12-6"/></svg></div><div class="why-name">Competitive Pricing</div><div class="why-more">Learn More</div></div>
<div class="why-box" style="left:110px;top:1767px"><div class="why-icon"><svg width="40" height="40" viewBox="0 0 40 40" fill="none" stroke="#fff" stroke-width="2"><path d="M14 26a10 10 0 1112 0v5H14z"/><path d="M16 35h8"/></svg></div><div class="why-name">Customization</div><div class="why-more">Learn More</div></div>
<div class="why-box" style="left:445px;top:1767px"><div class="why-icon"><svg width="40" height="40" viewBox="0 0 40 40" fill="none" stroke="#fff" stroke-width="2"><circle cx="12" cy="12" r="5"/><circle cx="28" cy="12" r="5"/><circle cx="12" cy="28" r="5"/><circle cx="28" cy="28" r="5"/></svg></div><div class="why-name">Communication</div><div class="why-more">Learn More</div></div>
<div class="why-box" style="left:780px;top:1767px"><div class="why-icon"><svg width="40" height="40" viewBox="0 0 40 40" fill="none" stroke="#fff" stroke-width="2"><rect x="6" y="9" width="28" height="24" rx="2"/><path d="M6 16h28M13 5v7M27 5v7"/></svg></div><div class="why-name">Timely Completion</div><div class="why-more">Learn More</div></div>

<!-- services -->
<h2 class="h2 under" style="top:2123px;color:var(--navy)">Our <b>Services</b></h2>
<div class="arrow-c" style="left:41px"><svg width="10" height="10" viewBox="0 0 10 10"><path d="M7 1L3 5l4 4" stroke="#333" fill="none" stroke-width="1.5"/></svg></div>
<div class="arrow-c" style="left:1134px"><svg width="10" height="10" viewBox="0 0 10 10"><path d="M3 1l4 4-4 4" stroke="#333" fill="none" stroke-width="1.5"/></svg></div>

<div class="svc-card" style="left:110px">
  <div class="svc-img" style="background:linear-gradient(160deg,#7fa7c4,#4e5c4e 60%,#8b8d86)" role="img" aria-label="Camper van with solar panels parked in a forest"></div>
  <div class="svc-icon"><svg width="30" height="30" viewBox="0 0 30 30" fill="none" stroke="#fff" stroke-width="2"><path d="M4 14l11-9 11 9v12H4z"/><rect x="11" y="17" width="8" height="9"/></svg></div>
  <div class="svc-name">It's All Us! And Were Local</div>
  <p class="svc-text" style="top:274px">what does that meant in short, we do it all! Voranto power powered by, brightfield smart energy your entire solar project from a-z.</p>
  <div class="btn btn-orange" style="left:83px;top:362px;width:143px;height:48px">Learn More</div>
</div>
<div class="svc-card" style="left:445px">
  <div class="svc-img" style="background:linear-gradient(160deg,#6f9a3c,#d9a441 50%,#3b5e2d)" role="img" aria-label="Gold piggy bank with coins on a solar panel"></div>
  <div class="svc-icon dark"><svg width="30" height="30" viewBox="0 0 30 30" fill="none" stroke="#fff" stroke-width="2"><path d="M6 24l4-16h14l-4 16z"/><path d="M8 16h14M15 8l-3 16"/></svg></div>
  <div class="svc-name">$0.00 Out of Pocket</div>
  <p class="svc-text" style="top:274px">Yes It's True! Solar is Not Only Helping the Planet but It's Also Helping Your Wallet Homeowners</p>
  <div class="btn btn-navy" style="left:83px;top:362px;width:143px;height:48px">Learn More</div>
</div>
<div class="svc-card" style="left:780px">
  <div class="svc-img" style="background:linear-gradient(180deg,#5f97d3,#2d5b9a 55%,#1c3866)" role="img" aria-label="Solar technician kneeling on rooftop panels under a blue sky"></div>
  <div class="svc-icon"><svg width="30" height="30" viewBox="0 0 30 30" fill="none" stroke="#fff" stroke-width="2"><path d="M15 4l9 4v7c0 6-4 9-9 11-5-2-9-5-9-11V8z"/><path d="M11 15l3 3 5-6"/></svg></div>
  <div class="svc-name">Rest Assured We Have You Covered</div>
  <p class="svc-text" style="top:298px">what does that meant in short, we do it all! your entire solar project from a-z.</p>
  <div class="btn btn-orange" style="left:83px;top:362px;width:143px;height:48px">Learn More</div>
</div>

<!-- team -->
<div class="band" style="top:2764px;height:532px;background:linear-gradient(180deg,#173270,#142c63 60%,#0f2555)" role="img" aria-label="Dark blue tinted background of a house with a car at night"></div>
<h2 class="h2 under" style="top:2852px;color:#fff">How Our <b>Team Works?</b></h2>
<svg class="abs" style="left:0;top:2960px" width="1200" height="130" fill="none" stroke="#fff" stroke-width="1.2" stroke-dasharray="2 3" opacity=".8">
  <path d="M262 55 Q345 0 428 60"/><path d="M524 55 Q606 130 689 70"/><path d="M785 55 Q868 0 951 60"/>
</svg>
<div class="step" style="left:168px"><svg width="48" height="48" viewBox="0 0 48 48" fill="none" stroke="#fff" stroke-width="2"><circle cx="22" cy="22" r="13" stroke-dasharray="5 3"/><circle cx="22" cy="22" r="5"/><circle cx="34" cy="34" r="6"/></svg></div>
<div class="step" style="left:430px"><svg width="48" height="48" viewBox="0 0 48 48" fill="none" stroke="#fff" stroke-width="2"><path d="M8 20l16-12 16 12"/><rect x="11" y="20" width="26" height="20"/><path d="M18 26h12M18 32h12"/></svg></div>
<div class="step" style="left:691px"><svg width="48" height="48" viewBox="0 0 48 48" fill="none" stroke="#fff" stroke-width="2"><circle cx="24" cy="24" r="15"/><path d="M15 24h18M24 15v18"/></svg></div>
<div class="step" style="left:953px"><svg width="48" height="48" viewBox="0 0 48 48" fill="none" stroke="#fff" stroke-width="2"><rect x="8" y="8" width="12" height="12"/><rect x="28" y="8" width="12" height="12"/><circle cx="24" cy="34" r="7"/></svg></div>
<div class="step-label" style="left:84px">Site visit by our<br>expert</div>
<div class="step-label" style="left:346px">Scope of work<br>finalization</div>
<div class="step-label" style="left:607px">Quality Equipment and<br>timely Installation</div>
<div class="step-label" style="left:869px">Project<br>planning</div>

<!-- contact -->
<h2 class="h2" style="top:3376px;left:17px;color:var(--navy)"><b>Contact</b> Us</h2>
<div class="ci" style="top:3487px"><svg width="36" height="26" viewBox="0 0 36 26" fill="none" stroke="#fff" stroke-width="2.5"><rect x="2" y="2" width="32" height="22"/><path d="M2 2l16 13 16-13"/></svg></div>
<div class="ci-label" style="top:3484px">EMAIL:</div><div class="ci-text" style="top:3504px">info@companyname.com</div>
<div class="ci" style="top:3592px"><svg width="36" height="36" viewBox="0 0 24 24" fill="none" stroke="#fff" stroke-width="1.8"><path d="M6.6 10.8a15 15 0 006.6 6.6l2.2-2.2a1 1 0 011-.25 11 11 0 003.5.56 1 1 0 011 1V20a1 1 0 01-1 1A17 17 0 013 4a1 1 0 011-1h3.5a1 1 0 011 1 11 11 0 00.56 3.5 1 1 0 01-.25 1z"/></svg></div>
<div class="ci-label" style="top:3589px">PHONE:</div><div class="ci-text" style="top:3609px">(555) 521-3528</div>
<div class="ci" style="top:3685px"><svg width="30" height="36" viewBox="0 0 30 36" fill="none" stroke="#fff" stroke-width="2.5"><path d="M15 33S4 21 4 13a11 11 0 0122 0c0 8-11 20-11 20z"/><circle cx="15" cy="13" r="4"/></svg></div>
<div class="ci-label" style="top:3681px">ADDRESS:</div><div class="ci-text" style="top:3701px">0123 W. Company Name.<br>#1012 Linden Falls, CA 1234</div>

<div class="field" style="left:485px;top:3467px;width:282px;height:49px">First Name</div>
<div class="field" style="left:778px;top:3467px;width:284px;height:49px">Last Name</div>
<div class="field" style="left:485px;top:3531px;width:282px;height:49px">Phone Number</div>
<div class="field" style="left:778px;top:3531px;width:284px;height:49px">Email</div>
<div class="field" style="left:485px;top:3596px;width:577px;height:110px">Message</div>
<div class="btn btn-orange" style="left:487px;top:3733px;width:143px;height:48px">Submit Now</div>

<!-- footer -->
<footer class="footer">
  <div class="abs" style="left:130px;top:120px;font-size:44px;font-weight:500;letter-spacing:3px;line-height:1">VORANTO</div>
  <div class="abs" style="left:212px;top:170px;font-size:14px;letter-spacing:12px">POWER</div>
  <div class="f-h" style="left:491px">Quick Links</div>
  <ul class="f-links"><li>Home</li><li>About Us</li><li>Services</li><li>Contact Us</li></ul>
  <div class="f-h" style="left:733px;top:60px">Contact Us</div>
  <div class="f-dot" style="top:102px"><svg width="14" height="18" viewBox="0 0 30 36" fill="none" stroke="#fff" stroke-width="4"><path d="M15 33S4 21 4 13a11 11 0 0122 0c0 8-11 20-11 20z"/></svg></div>
  <div class="f-text" style="top:108px">48 Elm Grove Ave.Suite 12<br>Maple Center,NY 10101<br>USA</div>
  <div class="f-dot" style="top:203px"><svg width="18" height="18" viewBox="0 0 24 24" fill="#fff"><path d="M6.6 10.8a15 15 0 006.6 6.6l2.2-2.2a1 1 0 011-.25 11 11 0 003.5.56 1 1 0 011 1V20a1 1 0 01-1 1A17 17 0 013 4a1 1 0 011-1h3.5a1 1 0 011 1 11 11 0 00.56 3.5 1 1 0 01-.25 1z"/></svg></div>
  <div class="f-text" style="top:208px">TEL: 555.255.0600<br>FAX: 555.255.0605</div>
  <div class="abs" style="left:98px;top:366px;width:1003px;height:1px;background:rgba(255,255,255,.6)"></div>
  <div class="abs" style="left:0;top:388px;width:1200px;text-align:center;font-size:14.5px">Copyrights@2025.Company Name.All Rights Reserved</div>
</footer>
<div class="social" style="left:157px;background:var(--orange);border-color:var(--orange)"></div>
<div class="social" style="left:203px"></div>
<div class="social" style="left:249px"></div>
<div class="social" style="left:295px"></div>

</body>
</html>
```